Flyer to Advertise Eyelash Extension Training Courses for Beauty Industry Professionals and Future

Hello,

I own an Eyelash and Skincare studio in Aliso Viejo, CA. www.lumenvaleaesthetics.com.We are now about to be offering a education side to our company where we offer courses to other beauty industry professionals or cosmetology students/future professionals. It will be called LVA ACADEMY. Our academies will have certain dates that will be on our website. I would like to make a flyer/menu of our new courses. You don't have to use all the information below but I've made it available for you. Please Re-word if necessary. Also you don't have to use the photos i've attached there just to help you see what I'm doing. Also I love the Look of Grant Holloway brands, Verosse, TOV, KELO, so I want this flyer to look really appealing to beauty industry professionals and future professionals.So be as creative as possible.

We have these courses:

1) Eyelash Enhancement Classic Extension Course
-1 Day Course. $350 and comes with a Kit that should last the students through 30 clients.
2) Eyelash Enhancement Russian Volume Course
-2 Day Course. $450 and comes with a kit that should last the students through 30 clients.
3)Threading Hair Removal Course
-1/2 Day course. $100 and comes with a kit that should last students through 60 clients. Students will need 3 Models for Eyebrow Threading
4)Spray Tanning Course
-1/2 Day course. $100 and will have an "add-on" kit that will get them a Spray tan Machine with 3 basic colors to last the student through 300 clients.

BUNDLE DEALS:
-Lash Pro Bundle: Students will learn Eyelash Enhancement Both Classic and Volume Extensions. 4 Day Course. $650 and comes with 2 kits for each technique.
-Lumen Pro Bundle: All of our courses combined. $850

MOBILE Options:
Call 949-637-2081 to inquire or email kelseymarlowe@lumenvaleaesthetics.com

Target Market(s)

Cosmetology Schools, Beauty Industry Students, Beauty industry professionals looking to seek add on services to provide to their clients.

Industry/Entity Type

Cosmetology

Font styles to use
Serif
Sans Serif
Decorative

Colors
f59296
f04a50
ffffff
000000
5c5c5c
aaaaaa

Requirements
Must have
• logo, all the courses, and our phone number email and address.
Nice to have
• pricing, and maybe saying something like, Additional courses insure that you are providing as many services as possible to your clients and in return you gain customer loyalty. (Reword)
Should not have
• cheesy.

```html
<!DOCTYPE html>
<html lang="en">
<head>
<meta charset="utf-8">
<title>LVA Academy – Eyelash &amp; Skincare Courses</title>
<link rel="stylesheet" href="https://fonts.googleapis.com/css2?family=Great+Vibes&family=Oswald:wght@200;300;400;500;600;700&family=Roboto+Condensed:wght@400;500;700&display=swap">
<style>
  :root {
    --blush: #f59296;
    --coral: #f04a50;
    --white: #ffffff;
    --black: #000000;
    --graphite: #5c5c5c;
    --silver: #aaaaaa;
    --ink: #141414;
    --script: 'Great Vibes', cursive;
    --display: 'Oswald', sans-serif;
    --body: 'Roboto Condensed', sans-serif;
  }
  * { box-sizing: border-box; margin: 0; padding: 0; }
  html, body { width: 849px; height: 1200px; overflow: hidden; background: var(--ink); }
  .flyer {
    position: relative;
    width: 849px;
    height: 1200px;
    overflow: hidden;
    background: linear-gradient(180deg, #3a3a3a 0%, #333333 45%, #1e1e1e 75%, #0e0e0e 100%);
    font-family: var(--body);
    color: var(--white);
  }

  /* Hero photograph area */
  .hero-photo {
    position: absolute;
    inset: 0 0 auto 0;
    height: 600px;
    background:
      linear-gradient(100deg,
        #6e2a22 0%, #d8463c 14%, #c23a32 24%, #8e5a48 34%,
        #d7ad94 46%, #e6c4ad 56%, #ede4d6 68%, #f3ede3 80%, #b9aa96 100%);
  }
  .hero-photo::after {
    content: "";
    position: absolute;
    inset: 0;
    background: linear-gradient(180deg, rgba(58,58,58,0) 30%, rgba(58,58,58,.55) 55%, rgba(51,51,51,.92) 78%, #333333 100%);
  }

  /* Headline */
  .headline {
    position: absolute;
    left: 0; right: 0;
    top: 330px;
    text-align: center;
  }
  .headline__script {
    font-family: var(--script);
    font-size: 52px;
    line-height: 1;
    color: var(--white);
  }
  .headline__brand {
    position: relative;
    display: inline-block;
    margin-top: 2px;
    font-family: var(--display);
    font-weight: 200;
    font-size: 104px;
    line-height: 1;
    letter-spacing: 5px;
    color: var(--white);
  }
  .headline__stroke {
    position: absolute;
    left: -30px;
    top: 44px;
    width: 480px;
    height: 30px;
    z-index: 0;
  }
  .headline__text { position: relative; z-index: 1; }

  /* Course cards */
  .courses {
    position: absolute;
    left: 46px;
    top: 546px;
    display: flex;
    gap: 11px;
  }
  .course {
    width: 182px;
    height: 488px;
    border-radius: 16px;
    overflow: hidden;
    border: 2px solid rgba(255,255,255,.85);
    background: linear-gradient(180deg, #262626 0%, #3a3a3a 22%, #9a9a9a 42%, #f0f0f0 56%, #ffffff 100%);
    display: flex;
    flex-direction: column;
    box-shadow: 0 6px 16px rgba(0,0,0,.5);
  }
  .course__photo { height: 202px; flex: none; }
  .course__photo--classic   { background: linear-gradient(135deg, #f1d2bd 0%, #d9a58b 45%, #a9705c 80%, #6a4437 100%); }
  .course__photo--volume    { background: linear-gradient(135deg, #f2c7ae 0%, #e0a283 40%, #c07b66 75%, #8e4f45 100%); }
  .course__photo--threading { background: linear-gradient(135deg, #c9ccd0 0%, #e2d9d0 40%, #b7a89c 70%, #74706c 100%); }
  .course__photo--tanning   { background: linear-gradient(135deg, #f0e3cf 0%, #d7a682 38%, #b8705a 68%, #e9dcc6 100%); }
  .course__body {
    flex: 1;
    padding: 14px 14px 0;
    text-align: center;
  }
  .course__title {
    font-family: var(--display);
    font-weight: 600;
    font-size: 19px;
    line-height: 1.22;
    color: var(--coral);
    min-height: 126px;
  }
  .course__title--short { min-height: 76px; }
  .course__length {
    font-family: var(--display);
    font-weight: 300;
    font-size: 13.5px;
    color: var(--black);
    text-transform: uppercase;
    margin-top: 4px;
  }
  .course__price {
    font-family: var(--display);
    font-weight: 700;
    font-size: 29px;
    line-height: 1.05;
    color: var(--black);
  }
  .course__detail {
    font-family: var(--body);
    font-weight: 500;
    font-size: 12.5px;
    line-height: 1.5;
    color: var(--black);
    margin-top: 4px;
  }

  /* Studio name */
  .brand {
    position: absolute;
    left: 0; right: 0;
    top: 1050px;
    text-align: center;
    line-height: 1;
  }
  .brand__mark {
    display: block;
    width: 28px; height: 28px;
    margin: 0 auto 8px;
    border-radius: 50%;
    border: 2px solid var(--white);
  }
  .brand__name {
    font-family: var(--display);
    font-weight: 400;
    font-size: 38px;
    letter-spacing: 3px;
    color: var(--white);
  }
  .brand__sub {
    display: block;
    font-size: 15px;
    letter-spacing: 4px;
    margin-top: 2px;
  }

  /* Footer */
  .footer-rule {
    position: absolute;
    left: 0; right: 0;
    top: 1140px;
    height: 6px;
    background: var(--coral);
  }
  .footer {
    position: absolute;
    left: 0; right: 0;
    top: 1146px;
    bottom: 0;
    background: var(--black);
    display: flex;
    align-items: center;
    padding: 0 0 0 110px;
    font-family: var(--body);
    font-size: 12.5px;
    color: var(--white);
  }
  .footer__item + .footer__item::before {
    content: "";
    display: inline-block;
    width: 7px; height: 7px;
    background: var(--white);
    margin: 0 10px 1px;
  }
  .footer__social { margin-left: 46px; display: flex; gap: 14px; }
  .footer__social span {
    width: 20px; height: 20px;
    border-radius: 3px;
    background: var(--white);
  }
</style>
</head>
<body>
<main class="flyer">
  <div class="hero-photo" role="img" aria-label="Smiling woman in a straw sun hat smelling red flowers"></div>

  <header class="headline">
    <p class="headline__script">Eyelash &amp; Skincare courses</p>
    <h1 class="headline__brand">
      <svg class="headline__stroke" viewBox="0 0 480 30" preserveAspectRatio="none" aria-hidden="true">
        <path d="M2 12 Q120 4 260 7 T478 8 L470 22 Q330 27 170 24 T10 25 Z" fill="var(--coral)"/>
      </svg>
      <span class="headline__text">LVA ACADEMY</span>
    </h1>
  </header>

  <section class="courses">
    <article class="course">
      <div class="course__photo course__photo--classic" role="img" aria-label="Close-up of a closed eye with classic lash extensions"></div>
      <div class="course__body">
        <h2 class="course__title">Eyelash<br>Enhancement<br>Classic<br>Extension<br>Course</h2>
        <p class="course__length">1 Day Course.</p>
        <p class="course__price">$350</p>
        <p class="course__detail">and comes with a Kit that should last the students through 30 clients.</p>
      </div>
    </article>
    <article class="course">
      <div class="course__photo course__photo--volume" role="img" aria-label="Close-up of an eye with Russian volume lash extensions"></div>
      <div class="course__body">
        <h2 class="course__title">Eyelash<br>Enhancement<br>Russian<br>Volume<br>Course</h2>
        <p class="course__length">2 Day Course.</p>
        <p class="course__price">$450</p>
        <p class="course__detail">and comes with a kit that should last the students through 30 clients.</p>
      </div>
    </article>
    <article class="course">
      <div class="course__photo course__photo--threading" role="img" aria-label="Lash strips laid out on a hand for practice"></div>
      <div class="course__body">
        <h2 class="course__title course__title--short">Threading<br>Hair Removal<br>Course</h2>
        <p class="course__length">1/2 Day Course.</p>
        <p class="course__price">$100</p>
        <p class="course__detail">and comes with a kit<br>that should last students<br>through 60 clients.<br>Students will need<br>3 Models for Eyebrow<br>Threading.</p>
      </div>
    </article>
    <article class="course">
      <div class="course__photo course__photo--tanning" role="img" aria-label="Tanned woman lying on the beach"></div>
      <div class="course__body">
        <h2 class="course__title course__title--short">Spray<br>Tanning<br>Course</h2>
        <p class="course__length">1/2 Day Course.</p>
        <p class="course__price">$100</p>
        <p class="course__detail">and will have an “add-on”<br>kit that will get them a<br>Spray tan Machine with<br>3 basic colors to last the<br>student through<br>300 clients.</p>
      </div>
    </article>
  </section>

  <div class="brand">
    <span class="brand__mark" aria-hidden="true"></span>
    <p class="brand__name">LUMEN VALE<span class="brand__sub">AESTHETICS</span></p>
  </div>

  <div class="footer-rule"></div>
  <footer class="footer">
    <span class="footer__item">418 Corvel Lane, Aliso Viejo, CA 92656</span>
    <span class="footer__item">949-637-2081</span>
    <span class="footer__item">studio@lumenvaleaesthetics.com</span>
    <span class="footer__social" aria-label="Social media"><span></span><span></span><span></span></span>
  </footer>
</main>
</body>
</html>
```